Spring Exterior Painting Advertisement

Attached is the postcard that we used last year(file - pixelharbor_318939...vector....pdf.. The information contained will be the same except for it will be updated for use during the spring of 2023.

The second attachment (sept 2021mailer) is another design that we've used in the past.

```html
<!DOCTYPE html>
<html lang="en">
<head>
<meta charset="utf-8">
<title>Keystone Painting – Spring Exterior Postcard</title>
<link href="https://fonts.googleapis.com/css2?family=Poppins:wght@500;600;700;800&display=swap" rel="stylesheet">
<style>
  :root{
    --brand-blue:#0b6a97;
    --brand-gold:#e8ab25;
    --ink:#262626;
    --paper:#ffffff;
    --backdrop:#ececec;
    --stamp:#dcdcdc;
    --rule:#c9c9c9;
  }
  *{box-sizing:border-box;margin:0;padding:0}
  html,body{width:1200px;height:2662px;overflow:hidden}
  body{background:var(--backdrop);font-family:'Poppins',sans-serif;color:var(--ink);position:relative}

  .postcard{position:absolute;left:99px;width:1002px;height:668px;background:var(--paper);box-shadow:0 4px 14px rgba(0,0,0,.18)}
  .postcard--front{top:630px}
  .postcard--back{top:1364px}

  .brand{display:flex;align-items:center;gap:10px;font-weight:800;color:var(--ink);letter-spacing:1px;white-space:nowrap}
  .brand__mark{background:var(--ink);flex:none}

  /* front */
  .hero-photo{position:absolute;left:31px;top:30px;width:938px;height:417px;
    background:linear-gradient(180deg,#d9e6f1 0%,#b9cadb 30%,#8e9a78 58%,#5d6b45 82%,#3d4a2c 100%)}
  .hero-photo .brand{position:absolute;left:50%;top:40px;transform:translateX(-50%);font-size:34px}
  .hero-photo .brand__mark{width:40px;height:40px}

  .offer-band{position:absolute;left:31px;top:447px;width:938px;height:123px;display:flex}
  .offer-band__headline{width:537px;background:var(--brand-blue);padding:14px 0 0 42px;font-weight:800;line-height:1;text-transform:uppercase}
  .offer-band__headline .line-gold{color:var(--brand-gold);font-size:45px;display:block}
  .offer-band__headline .line-white{color:#fff;font-size:47px;display:block;margin-top:2px}
  .offer-band__deal{flex:1;background:var(--brand-gold);position:relative}
  .deal__save{position:absolute;left:64px;top:10px;width:270px;height:54px;background:var(--brand-blue);border-radius:4px 18px 18px 4px;color:#fff;font-weight:800;font-size:42px;line-height:54px;padding-left:34px}
  .deal__code{position:absolute;left:78px;top:72px;display:flex;font-weight:700;font-size:17px;height:24px;line-height:24px}
  .deal__code-label{background:var(--brand-blue);color:#fff;padding:0 16px}
  .deal__code-value{background:#fff;color:var(--ink);padding:0 10px}
  .deal__expiry{position:absolute;left:130px;top:100px;font-size:13px;font-weight:700;color:var(--ink)}

  .contact-strip{position:absolute;left:48px;top:590px;width:900px;display:flex;align-items:center;font-weight:600;font-size:27px;color:var(--ink)}
  .contact-strip .icon-dot{width:34px;height:34px;border-radius:50%;background:var(--brand-gold);display:inline-flex;align-items:center;justify-content:center;margin-right:16px;flex:none}
  .contact-strip .phone{margin-right:18px}
  .contact-strip .web{font-size:26px;margin-right:18px;display:flex;align-items:center}
  .contact-strip .web .icon-dot{margin-right:8px}
  .follow-pill{background:var(--brand-blue);color:#fff;border-radius:20px;font-size:18px;font-weight:500;padding:4px 14px;display:flex;align-items:center;gap:7px}
  .follow-pill i{display:block;width:20px;height:20px;border-radius:50%;background:#fff}

  /* back */
  .quote-panel{position:absolute;left:14px;top:21px;width:469px;height:623px}
  .quote-panel__title{height:106px;background:var(--brand-gold);color:#fff;font-weight:800;font-size:36px;line-height:1.02;padding:20px 0 0 29px;text-transform:uppercase}
  .quote-panel__body{height:358px;background:var(--brand-blue);position:relative;color:#fff}
  .years-badge{position:absolute;left:32px;top:10px;width:114px;height:114px;border-radius:50%;background:#fff;color:var(--brand-blue);text-align:center}
  .years-badge__num{position:absolute;left:18px;top:14px;font-size:50px;font-weight:700;line-height:1}
  .years-badge__tag{position:absolute;left:68px;top:42px;background:var(--brand-gold);color:#fff;font-size:11px;font-weight:700;padding:0 2px}
  .years-badge__label{position:absolute;left:0;right:0;top:72px;font-size:15px;font-weight:600}
  .quote-panel__intro{position:absolute;left:156px;top:10px;width:300px;font-size:15.3px;font-weight:600;line-height:1.27}
  .services{position:absolute;left:38px;top:146px;display:grid;grid-template-columns:236px 180px;row-gap:14px}
  .service{display:flex;align-items:center;gap:11px;font-size:14.5px;font-weight:600;line-height:1.3;text-transform:uppercase;height:52px}
  .service__icon{width:52px;height:52px;border-radius:50%;background:#fff;border:4px solid var(--brand-gold);flex:none;display:flex;align-items:center;justify-content:center}
  .service__icon span{width:20px;height:20px;background:var(--brand-blue);border-radius:3px}
  .quote-panel__contact{height:159px;background:var(--brand-gold);color:#fff;padding:18px 0 0 32px;font-size:23px;font-weight:500;line-height:1.05}
  .quote-panel__contact li{list-style:none;display:flex;gap:9px;margin-bottom:8px}
  .quote-panel__contact .bullet{width:24px;height:24px;border-radius:50%;background:var(--brand-blue);flex:none;margin-top:2px}
  .quote-panel__contact .strong{font-weight:700}

  .address-side .brand{position:absolute;left:538px;top:88px;font-size:22px;letter-spacing:.5px}
  .address-side .brand__mark{width:28px;height:28px}
  .stamp-box{position:absolute;left:839px;top:48px;width:113px;height:113px;background:var(--stamp)}
  .address-line{position:absolute;left:574px;width:378px;height:1px;background:var(--rule)}
</style>
</head>
<body>

<section class="postcard postcard--front" aria-label="Postcard front">
  <div class="hero-photo" role="img" aria-label="Photo of a two-storey sage green house with dark shutters, white picket fence and evergreen trees under a light sky">
    <div class="brand"><span class="brand__mark"></span>KEYSTONE PAINTING</div>
  </div>
  <div class="offer-band">
    <div class="offer-band__headline">
      <span class="line-gold">Exterior Job</span>
      <span class="line-white">Get Painted Now!</span>
    </div>
    <div class="offer-band__deal">
      <div class="deal__save">SAVE 15%</div>
      <div class="deal__code"><span class="deal__code-label">COUPON CODE</span><span class="deal__code-value">"EXT2023"</span></div>
      <div class="deal__expiry">EXPIRES 15.05.2023</div>
    </div>
  </div>
  <div class="contact-strip">
    <span class="icon-dot">
      <svg width="18" height="18" viewBox="0 0 24 24"><path fill="#fff" d="M6.6 10.8a15 15 0 0 0 6.6 6.6l2.2-2.2a1 1 0 0 1 1-.25 11.4 11.4 0 0 0 3.6.57 1 1 0 0 1 1 1V20a1 1 0 0 1-1 1A17 17 0 0 1 3 4a1 1 0 0 1 1-1h3.5a1 1 0 0 1 1 1c0 1.25.2 2.45.57 3.570a1 1 0 0 1-.25 1z"/></svg>
    </span>
    <span class="phone">555-014-2287</span>
    <span class="web"><span class="icon-dot">
      <svg width="18" height="18" viewBox="0 0 24 24" fill="none" stroke="#fff" stroke-width="2"><circle cx="12" cy="12" r="9"/><path d="M3 12h18M12 3c3 3.5 3 14.5 0 18M12 3c-3 3.5-3 14.5 0 18"/></svg>
    </span>www.keystonepaintingco.com</span>
    <span class="follow-pill">follow us <i></i><i></i></span>
  </div>
</section>

<section class="postcard postcard--back" aria-label="Postcard back">
  <div class="quote-panel">
    <h2 class="quote-panel__title">Request your<br>free Keystone quote</h2>
    <div class="quote-panel__body">
      <div class="years-badge">
        <span class="years-badge__num">19</span>
        <span class="years-badge__tag">YERAS</span>
        <span class="years-badge__label">BUSINESS</span>
      </div>
      <p class="quote-panel__intro">Keystone Painting’s local team offers professional painting for your home's exterior and interior surfaces. With over 19 years in business, we offer skillfulworkmanship backed by a three-year warranty.</p>
      <div class="services">
        <div class="service"><span class="service__icon"><span></span></span>Pressure<br>washing</div>
        <div class="service"><span class="service__icon"><span></span></span>Interior<br>painting</div>
        <div class="service"><span class="service__icon"><span></span></span>Exterior painting<br>&amp; staining</div>
        <div class="service"><span class="service__icon"><span></span></span>Cabinetry<br>finishing</div>
        <div class="service"><span class="service__icon"><span></span></span>Color<br>consultations</div>
        <div class="service"><span class="service__icon"><span></span></span>Carpentry</div>
      </div>
    </div>
    <ul class="quote-panel__contact">
      <li><span class="bullet"></span><span class="strong">555-014-2287</span></li>
      <li><span class="bullet"></span><span>18 Harbor Ln. Unit B<br>Lakeview, WI 53000</span></li>
      <li><span class="bullet"></span><span>www.keystonepaintingco.com</span></li>
    </ul>
  </div>
  <div class="address-side">
    <div class="brand"><span class="brand__mark"></span>KEYSTONE PAINTING</div>
    <div class="stamp-box"></div>
    <div class="address-line" style="top:305px"></div>
    <div class="address-line" style="top:368px"></div>
    <div class="address-line" style="top:431px"></div>
  </div>
</section>

</body>
</html>
```